Kindled Lantern; The Road of the Quiet Lantern

Kindled Lantern needs a banner ad design that can be used for social media campaigns and sites. KL's mission is to bring spiritual and mindfulness to veterans, first responders and survivors of trauma. We are looking for a design that represents the strength of this community (warriors) and the connection to spirituality. Also needs to include the KL logo of the tree of life (see attached).

Kindled Lantern’s mission is to honor, support, and empower warriors to build the life skills needed to integrate and thrive in the world. We provide spiritual support to Veterans, First Responders, and their families through guidance, education, and advocacy.

As a veteran owned company, we know it’s impossible to explain the sacrifices required by those who serve their country. To share the wounds and scars that come from putting service before your family, friends, and yourself. To make yourself vulnerable by opening up to people who haven’t experienced what you have experienced.

Our mission is to improve the quality of life of those who have sacrificed for others by providing revolutionary spiritual services developed by and geared towards warriors.

Target Market(s)

Spiritual warriors, veterans, first responders, and survivors of trauma

Industry/Entity Type

Health And Wellness

Font styles to use
Decorative
Script

Colors
ffcf3e
ffffff

Requirements
Must have
• Main colors, Black, white, gold. Looking for something that signifies warriors. Spiritual warriors preferable. Shows strength, displine, and spiritual connection.
Nice to have
• pop of color is fine
Should not have
• Not just American soldiers, so stay away from red-white and blue

```html
<!DOCTYPE html>
<html lang="en">
<head>
<meta charset="utf-8">
<title>Kindled Lantern — Banner Set</title>
<link rel="stylesheet" href="https://fonts.googleapis.com/css2?family=Cinzel:wght@400;600&family=Yesteryear&family=Arimo&display=swap">
<style>
  :root {
    --ink: #000000;
    --paper: #ffffff;
    --gold: #ffcf3e;
    --gold-deep: #c99a2e;
    --label: #111111;
    --frame: #555555;
    --photo-light: #dcd8ce;
    --photo-mid: #8f8a7c;
    --photo-dark: #3b3934;
  }
  html, body {
    margin: 0;
    padding: 0;
    overflow: hidden;
    background: var(--paper);
  }
  .sheet {
    position: relative;
    width: 1200px;
    height: 1200px;
    overflow: hidden;
    background: var(--paper);
  }
  .banner {
    position: absolute;
    display: block;
    outline: 1.2px solid var(--frame);
  }
  .banner--wide   { left: 28px;  top: 20px;  width: 720px; height: 378px; }
  .banner--square { left: 28px;  top: 419px; width: 720px; height: 719px; }
  .banner--tall   { left: 802px; top: 329px; width: 360px; height: 719px; }

  .brand-name {
    font-family: "Cinzel", serif;
    font-weight: 600;
    fill: var(--gold-deep);
    letter-spacing: 0.02em;
  }
  .tagline {
    font-family: "Cinzel", serif;
    font-weight: 400;
    fill: var(--paper);
  }
  .pillars {
    font-family: "Yesteryear", cursive;
    fill: var(--ink);
  }
  .label {
    position: absolute;
    font-family: "Arimo", sans-serif;
    font-size: 24px;
    line-height: 34px;
    color: var(--label);
    margin: 0;
  }
  .label--wide   { left: 812px; top: 108px; }
  .label--square { left: 28px; top: 1150px; width: 750px; text-align: center; }
  .label--tall   { left: 780px; top: 1070px; width: 420px; text-align: center; }
  .label-arrow {
    position: absolute;
    left: 758px;
    top: 130px;
    width: 40px;
    height: 30px;
  }
</style>
</head>
<body>
<main class="sheet">

  <!-- Wide banner -->
  <svg class="banner banner--wide" viewBox="0 0 600 315" xmlns="http://www.w3.org/2000/svg">
    <defs>
      <linearGradient id="photoToneWide" x1="0" y1="0" x2="1" y2="0">
        <stop offset="0" stop-color="var(--photo-light)"/>
        <stop offset="0.6" stop-color="var(--photo-mid)"/>
        <stop offset="1" stop-color="var(--photo-dark)"/>
      </linearGradient>
    </defs>
    <rect class="field" width="600" height="315" fill="var(--paper)"/>
    <polygon class="band-dark" points="0,0 600,0 600,280 477,280 447,123 80,84 0,84" fill="var(--ink)"/>
    <polygon class="band-gold" points="0,48 85,55 0,280" fill="var(--gold)"/>
    <polygon class="photo" points="30,60 125,60 135,0 150,0 230,210 232,315 30,315" fill="url(#photoToneWide)" role="img" aria-label="Photo of an honor guard veteran in white uniform holding a flag"/>
    <text class="brand-name" x="390" y="62" font-size="30" text-anchor="middle">KINDLED LANTERN</text>
    <text class="tagline" x="390" y="85" font-size="10.5" text-anchor="middle">Bonded in war, bonded in healing, brothers and sisters in arms</text>
    <circle class="brand-mark" cx="527" cy="160" r="50" fill="none" stroke="var(--gold-deep)" stroke-width="2"/>
    <text class="pillars" font-size="22">
      <tspan x="238" y="183">Spiritual Connection,</tspan>
      <tspan x="238" y="218">Discipline,</tspan>
      <tspan x="238" y="254">Strength for Warriors</tspan>
    </text>
  </svg>

  <svg class="label-arrow" viewBox="0 0 40 30" xmlns="http://www.w3.org/2000/svg" aria-hidden="true">
    <path d="M38 15 H4 M14 5 L4 15 L14 25" fill="none" stroke="var(--label)" stroke-width="3"/>
  </svg>
  <p class="label label--wide">600X315&nbsp; landscape<br>for Circlebook and Snapframe</p>

  <!-- Square banner -->
  <svg class="banner banner--square" viewBox="0 0 600 599" xmlns="http://www.w3.org/2000/svg">
    <defs>
      <linearGradient id="photoToneSquare" x1="0" y1="0" x2="1" y2="0">
        <stop offset="0" stop-color="var(--photo-light)"/>
        <stop offset="0.6" stop-color="var(--photo-mid)"/>
        <stop offset="1" stop-color="var(--photo-dark)"/>
      </linearGradient>
    </defs>
    <rect class="field" width="600" height="599" fill="var(--paper)"/>
    <polygon class="band-dark" points="0,0 600,0 600,378 485,315 440,140 0,103" fill="var(--ink)"/>
    <polygon class="band-gold" points="0,104 140,128 20,599 0,599" fill="var(--gold)"/>
    <polygon class="photo" points="10,240 110,240 120,128 170,128 262,380 270,599 10,599" fill="url(#photoToneSquare)" role="img" aria-label="Photo of an honor guard veteran in white uniform holding a flag"/>
    <text class="brand-name" x="300" y="62" font-size="40" text-anchor="middle">KINDLED LANTERN</text>
    <text class="tagline" x="300" y="93" font-size="13" text-anchor="middle">Bonded in war, bonded in healing, brothers and sisters in arms</text>
    <circle class="brand-mark" cx="530" cy="210" r="58" fill="none" stroke="var(--gold-deep)" stroke-width="2.5"/>
    <text class="pillars" font-size="38">
      <tspan x="280" y="400">Spiritual Connection,</tspan>
      <tspan x="280" y="448">Discipline,</tspan>
      <tspan x="280" y="496">Strength for Warriors</tspan>
    </text>
  </svg>
  <p class="label label--square">600X600&nbsp; Landscape Snapframe as bonus</p>

  <!-- Tall banner -->
  <svg class="banner banner--tall" viewBox="0 0 300 599" xmlns="http://www.w3.org/2000/svg">
    <defs>
      <linearGradient id="photoToneTall" x1="0" y1="0" x2="1" y2="0">
        <stop offset="0" stop-color="var(--photo-dark)"/>
        <stop offset="0.5" stop-color="var(--photo-mid)"/>
        <stop offset="1" stop-color="var(--photo-light)"/>
      </linearGradient>
    </defs>
    <rect class="field" width="300" height="599" fill="var(--paper)"/>
    <polygon class="band-gold" points="0,441 300,572 300,599 0,599" fill="var(--gold)"/>
    <polygon class="photo" points="0,110 100,110 108,300 112,492 0,441" fill="url(#photoToneTall)" role="img" aria-label="Photo of a flag on a pole with gold fringe"/>
    <polygon class="band-dark" points="0,0 300,0 300,108 297,110 150,252 87,125 0,110" fill="var(--ink)"/>
    <text class="brand-name" x="150" y="36" font-size="23" text-anchor="middle">KINDLED LANTERN</text>
    <text class="tagline" font-size="12" text-anchor="middle">
      <tspan x="150" y="56">Bonded in war, bonded in healing,</tspan>
      <tspan x="150" y="73">brothers and sisters in arms</tspan>
    </text>
    <circle class="brand-mark" cx="155" cy="160" r="44" fill="none" stroke="var(--gold-deep)" stroke-width="2"/>
    <text class="pillars" font-size="16.5">
      <tspan x="118" y="310">Spiritual Connection,</tspan>
      <tspan x="118" y="343">Discipline,</tspan>
      <tspan x="118" y="380">Strength for Warriors</tspan>
    </text>
  </svg>
  <p class="label label--tall">300X600&nbsp; for Searchly Ads<br>on Streamhall</p>

</main>
</body>
</html>
```